Business Card Design Project

I would like to get a logo as well as business card and stationery.

i am in an event planner and coordination business. I need something sophisticated and elegant.

Business

```html
<!DOCTYPE html>
<html lang="en">
<head>
<meta charset="utf-8">
<title>Bellhaven Occasions – Business Card</title>
<link rel="stylesheet" href="https://fonts.googleapis.com/css2?family=Cormorant+Garamond:wght@500&family=Great+Vibes&family=Lato:wght@400&display=swap">
<style>
  :root {
    --backdrop: #e8e5e0;
    --card: #ffffff;
    --ink: #151515;
    --wordmark: #383838;
    --text: #2a2a2a;
    --stud: #4a4a4a;
  }
  html, body {
    margin: 0;
    padding: 0;
    width: 1200px;
    height: 851px;
    overflow: hidden;
    background: var(--backdrop);
  }
  .canvas { position: relative; width: 1200px; height: 851px; }
  .card {
    position: absolute;
    width: 540px;
    height: 324px;
    background: var(--card);
    box-shadow: 0 2px 8px rgba(0,0,0,0.12);
  }
  .card--front { left: 96px; top: 69px; }
  .card--back  { left: 499px; top: 420px; }
  .card__frame { position: absolute; inset: 0; width: 540px; height: 324px; }
  .stud {
    position: absolute;
    width: 9px;
    height: 9px;
    background: var(--stud);
    transform: translate(-50%, -50%) rotate(45deg);
  }
  .wordmark {
    position: absolute;
    left: 0;
    right: 0;
    margin: 0;
    text-align: center;
    font-family: "Cormorant Garamond", serif;
    font-weight: 500;
    color: var(--wordmark);
    white-space: nowrap;
  }
  .card--front .wordmark { top: 150px; font-size: 44px; line-height: 50px; letter-spacing: 1.5px; }
  .card--front .stud--top { left: 270px; top: 125px; }
  .card--front .stud--bottom { left: 270px; top: 216px; }
  .card--back .wordmark { top: 68px; font-size: 33px; line-height: 36px; letter-spacing: 1px; }
  .card--back .stud--left { left: 92px; top: 86px; }
  .card--back .stud--right { left: 462px; top: 86px; }
  .holder-name {
    position: absolute;
    left: 0;
    right: 0;
    top: 124px;
    margin: 0;
    text-align: center;
    font-family: "Great Vibes", cursive;
    font-size: 48px;
    line-height: 70px;
    color: var(--ink);
  }
  .holder-role {
    position: absolute;
    left: 0;
    right: 0;
    top: 215px;
    margin: 0;
    text-align: center;
    font-family: "Cormorant Garamond", serif;
    font-size: 13px;
    letter-spacing: 1px;
    text-transform: uppercase;
    color: var(--text);
  }
  .contact-line {
    position: absolute;
    left: 0;
    right: 0;
    top: 263px;
    margin: 0;
    text-align: center;
    font-family: "Lato", sans-serif;
    font-size: 10.5px;
    line-height: 16px;
    color: var(--text);
    white-space: nowrap;
  }
  .contact-line .sep { margin: 0 5px; }
</style>
</head>
<body>
<main class="canvas">

  <section class="card card--front" aria-label="Business card front">
    <svg class="card__frame" viewBox="0 0 540 324" aria-hidden="true">
      <rect x="28" y="27" width="483" height="269" fill="none" stroke="var(--ink)" stroke-width="3"/>
      <rect x="34" y="33" width="471" height="257" fill="none" stroke="var(--ink)" stroke-width="1"/>
      <path d="M40 100 V39 H102" fill="none" stroke="var(--ink)" stroke-width="1"/>
      <path d="M437 284 H499 V222" fill="none" stroke="var(--ink)" stroke-width="1"/>
    </svg>
    <span class="stud stud--top"></span>
    <h1 class="wordmark">Bellhaven Occasions</h1>
    <span class="stud stud--bottom"></span>
  </section>

  <section class="card card--back" aria-label="Business card back">
    <svg class="card__frame" viewBox="0 0 540 324" aria-hidden="true">
      <rect x="27" y="28" width="483" height="268" fill="none" stroke="var(--ink)" stroke-width="3"/>
      <rect x="33" y="34" width="471" height="256" fill="none" stroke="var(--ink)" stroke-width="1"/>
      <path d="M39 102 V40 H101" fill="none" stroke="var(--ink)" stroke-width="1"/>
      <path d="M436 284 H498 V222" fill="none" stroke="var(--ink)" stroke-width="1"/>
    </svg>
    <span class="stud stud--left"></span>
    <h2 class="wordmark">Bellhaven Occasions</h2>
    <span class="stud stud--right"></span>
    <p class="holder-name">Clara Whitfield</p>
    <p class="holder-role">Event Coordinator</p>
    <p class="contact-line">48 Mercer Street<span class="sep">|</span>New York, NY 10013<span class="sep">|</span>clara@bellhaven.co<span class="sep">|</span>212.555.0147<span class="sep">|</span>bellhaven.co</p>
  </section>

</main>
</body>
</html>
```